Health Benefits Association Website Design

The Allied Household Provision Association (AHPA) is an organization formed for the purpose of providing its members better value for selected health benefits and services. Members can use the association benefits either in conjunction with or independently of other medical insurance they may have. Some of the benefits available include discounted dental and vision care and prescription mail order services. There is no limitation on who can join. This membership will be primarily marketed as a way to enhance the value of a fixed benefit health insurance plan although members do not have to have the insurance plan join the association.

We are seeking a design for a website to be used for consumers to get information about membership and for current members to be able to access their benefits. The website should include:

1) A landing page to provide a description of the AHPA

2) A secondary page that can be duplicated that will:
a. Provide a list of benefits
b. Provide a membership enrollment form
c. Provide a member’s only access page
d. Provide a contact page for more information

We are seeking a modern but conservative design that will reflect value, simplicity and good health. The site design will also need to be compatible for use with mobile phones and tablets.

A copy of the association logo is included with the submission. It will also need to be incorporated into the website design. Layouts of similar association websites have also been included for reference.

Target Market(s)

Ages 25 to 65 unmarried, married with no children, professionals, self-employed, active and healthy

Industry/Entity Type

Health And Wellness

Number of Pages Required

2 page

Font styles to use
Sans Serif

Colors

Designer to choose colors to be used in the design.

Requirements
Must have
• AHPA Logo (attached). Use colors from the logo in the website design.
Nice to have
• Graphics, if used, should convey health and fitness and skew toward a diverse array of adults 25 to 40.

```html
<!DOCTYPE html>
<html lang="en">
<head>
<meta charset="utf-8">
<title>Allied Household Provision Association</title>
<link href="https://fonts.googleapis.com/css2?family=Cinzel:wght@400;700&family=Open+Sans:ital,wght@0,400;0,600;1,400&family=Roboto+Condensed:wght@300;400&display=swap" rel="stylesheet">
<style>
:root{
  --olive:#8a9a2d;
  --olive-dark:#6f7d1e;
  --yellow:#fed200;
  --cream:#fdfbe5;
  --ink:#2b2b2b;
  --text:#555;
  --white:#fff;
}
*{box-sizing:border-box;margin:0;padding:0}
html,body{width:1200px;height:2894px;overflow:hidden}
body{font-family:"Open Sans",sans-serif;color:var(--text);background:var(--white);position:relative}
.topbar{height:42px;background:var(--olive);display:flex;justify-content:flex-end;align-items:center;padding-right:78px;gap:20px;color:var(--white);font-size:15px}
.topbar span{display:flex;align-items:center;gap:10px}
.topbar .sep{width:1px;height:20px;background:rgba(255,255,255,.6)}
.header{height:103px;position:relative;display:flex;align-items:center}
.brand{position:absolute;left:66px;top:-34px;width:128px;height:128px;border-radius:50%;background:var(--white);display:flex;align-items:center;justify-content:center;text-align:center;font-family:"Cinzel",serif;font-weight:700;font-size:14px;line-height:1.2;color:var(--olive);padding:14px}
.nav{position:absolute;left:268px;top:30px;display:flex;align-items:center;gap:0;font-size:16px;color:#444}
.nav a{text-decoration:none;color:inherit;padding:0 13px;line-height:46px}
.nav a.active{background:var(--yellow);border-radius:23px;padding:0 24px;color:#222;margin-right:12px}
.btn{display:inline-block;background:var(--yellow);color:#222;font-family:"Cinzel",serif;font-weight:700;border-radius:30px;text-decoration:none;text-align:center}
.join{position:absolute;left:978px;top:26px;width:144px;height:56px;line-height:56px;font-size:22px}
.hero{height:533px;position:relative;background:linear-gradient(90deg,#f3f2dc 0%,#e9ead0 40%,#c9c49a 70%,#8b9170 100%)}
.hero .photo{position:absolute;inset:0}
.hero h1{position:absolute;left:78px;top:115px;font-family:"Roboto Condensed",sans-serif;font-weight:300;font-size:60px;line-height:64px;color:#1f1f1f}
.hero p{position:absolute;left:78px;top:258px;width:520px;font-style:italic;font-size:18px;line-height:28px;color:#333}
.hero .btn{position:absolute;left:78px;top:360px;width:175px;height:60px;line-height:60px;font-size:21px}
.arrow{position:absolute;top:245px;width:50px;height:50px;border-radius:50%;background:rgba(255,255,255,.45)}
.arrow.l{left:14px}.arrow.r{right:10px}
.section-mark{display:block;margin:0 auto;width:40px;height:40px;border-radius:50%;background:var(--olive)}
.section-title{font-family:"Cinzel",serif;color:var(--olive);font-size:44px;text-align:center;letter-spacing:2px}
.benefits{height:540px;background:var(--cream);padding-top:52px}
.benefits .section-title{margin-top:18px}
.benefit-row{display:flex;justify-content:space-between;padding:0 78px;margin-top:34px}
.benefit{width:255px;text-align:center}
.benefit .icon{width:136px;height:136px;border-radius:50%;background:var(--olive);margin:0 auto;display:flex;align-items:center;justify-content:center;box-shadow:-22px 22px 16px -14px rgba(0,0,0,.25)}
.benefit h3{font-family:"Cinzel",serif;font-size:21px;color:#222;margin-top:30px;letter-spacing:1px}
.benefit p{font-size:14px;line-height:27px;margin-top:20px}
.welcome{height:560px;position:relative}
.welcome .photo{position:absolute;left:690px;top:0;width:510px;height:560px;background:linear-gradient(160deg,#f4f4f2 0%,#d8d2cb 45%,#b7aba2 100%)}
.welcome .copy{position:absolute;left:78px;top:42px;width:585px}
.welcome .mark{width:40px;height:40px;border-radius:50%;background:var(--olive)}
.welcome .kicker{font-family:"Cinzel",serif;font-weight:700;font-size:19px;color:#222;margin-top:16px}
.welcome h2{font-family:"Cinzel",serif;font-weight:400;font-size:40px;color:var(--olive);margin-top:6px;letter-spacing:1px}
.welcome .sub{font-family:"Cinzel",serif;font-size:20px;color:var(--olive);opacity:.85;margin-top:4px}
.welcome p{font-size:14px;line-height:28px;margin-top:14px}
.welcome .btn{width:177px;height:56px;line-height:56px;font-size:21px;margin-top:22px}
.news{height:584px;background:var(--cream);padding-top:42px}
.news .section-title{margin-top:20px}
.news-row{display:flex;justify-content:space-between;padding:0 78px;margin-top:20px}
.post{width:333px}
.post .thumb{height:209px}
.post h3{font-family:"Cinzel",serif;font-weight:700;font-size:18px;color:var(--olive);margin-top:20px}
.post p{font-size:14px;line-height:27px;margin-top:10px}
.enroll{height:168px;background:var(--yellow);display:flex;align-items:center;padding-left:78px}
.enroll h2{font-family:"Cinzel",serif;font-weight:400;font-size:28px;line-height:42px;color:#222;width:302px;letter-spacing:1px}
.enroll .field{width:272px;height:56px;background:var(--white);margin-left:7px;font-size:13px;padding-left:14px;line-height:56px;color:#444}
.enroll .field:first-of-type{margin-left:0}
.enroll .outline{margin-left:14px;width:177px;height:56px;line-height:54px;border:2px solid #333;border-radius:30px;font-family:"Cinzel",serif;font-weight:700;font-size:21px;text-align:center;color:#222}
.footer{height:364px;background:var(--olive);position:relative;color:var(--white);font-size:14px}
.footer .brand-foot{position:absolute;left:110px;top:60px;width:180px;font-family:"Cinzel",serif;font-weight:700;font-size:24px;line-height:1.25;text-align:center;color:var(--white)}
.col{position:absolute;top:30px}
.col h4{font-family:"Cinzel",serif;font-weight:400;font-size:18px;color:var(--yellow);letter-spacing:1px;margin-bottom:16px}
.links{left:342px}
.links li{list-style:none;line-height:25px;display:flex;align-items:center;gap:12px}
.links li::before{content:"";width:8px;height:8px;border-radius:50%;background:var(--yellow)}
.events{left:607px;width:250px}
.events .item{line-height:26px;margin-bottom:12px}
.events .date{display:flex;align-items:center;gap:10px;color:var(--yellow);font-weight:600}
.contact{left:872px;width:260px}
.contact .row{display:flex;gap:14px;margin-bottom:14px;line-height:26px}
.contact .row svg{flex:none;margin-top:4px}
.contact strong{color:var(--yellow);font-weight:600}
.social{display:flex;gap:14px;margin-top:4px}
.social span{width:42px;height:42px;border-radius:50%;background:var(--yellow)}
.copyright{position:absolute;left:78px;right:78px;bottom:0;height:68px;border-top:1px solid rgba(255,255,255,.3);text-align:center;line-height:68px;font-size:13px}
</style>
</head>
<body>
<div class="topbar">
  <span><svg width="20" height="14" viewBox="0 0 20 14"><rect width="20" height="14" rx="2" fill="#fed200"/><path d="M1 1l9 7 9-7" stroke="#8a9a2d" stroke-width="2" fill="none"/></svg>info@alliedhousehold.org</span>
  <span class="sep"></span>
  <span><svg width="14" height="16" viewBox="0 0 14 16"><rect y="7" width="14" height="9" rx="1" fill="#fed200"/><path d="M3 7V5a4 4 0 018 0v2" stroke="#fed200" stroke-width="2" fill="none"/></svg>Login</span>
</div>
<header class="header">
  <div class="brand">Allied Household Provision Association</div>
  <nav class="nav">
    <a class="active">HOME</a><a>ABOUT</a><a>BENEFITS</a><a>NEWS</a><a>CHARITIES</a><a>MEMBERSHIP</a><a>CONTACT</a>
  </nav>
  <a class="btn join">JOIN US</a>
</header>
<section class="hero">
  <div class="photo" role="img" aria-label="Photo of a woman holding a tablet by a bright window"></div>
  <h1>The Allied Household<br>Provision Association</h1>
  <p>ASPA was started to be part of a senior-focused charitable organization that is different from other organizations with a similar perspective or mission.</p>
  <a class="btn">CONTACT US</a>
  <div class="arrow l"><svg width="50" height="50"><path d="M21 17l10 8-10 8z" fill="#8a9a2d"/></svg></div>
  <div class="arrow r"><svg width="50" height="50"><path d="M29 17l-10 8 10 8z" fill="#8a9a2d"/></svg></div>
</section>
<section class="benefits">
  <span class="section-mark"></span>
  <h2 class="section-title">OUR BENEFITS</h2>
  <div class="benefit-row">
    <div class="benefit">
      <div class="icon"><svg width="60" height="70" viewBox="0 0 60 70"><path d="M15 3c-9 0-13 8-12 17 1 10 6 14 7 24 1 12 4 23 9 23s5-17 11-17 6 17 11 17 8-11 9-23c1-10 6-14 7-24 1-9-3-17-12-17-6 0-10 4-15 4S21 3 15 3z" fill="#fff"/></svg></div>
      <h3>DENTAL</h3>
      <p>Lorem Ipsum is simply dummy text of the printing and typesetting industry. Lorem Ipsum has been.</p>
    </div>
    <div class="benefit">
      <div class="icon"><svg width="70" height="70" viewBox="0 0 70 70"><circle cx="32" cy="38" r="28" fill="#fff"/><circle cx="32" cy="38" r="19" fill="#8a9a2d"/><circle cx="32" cy="38" r="11" fill="#fff"/><circle cx="32" cy="38" r="4" fill="#8a9a2d"/><path d="M32 38L62 8" stroke="#fff" stroke-width="4"/><path d="M56 4l10 0-4 10z" fill="#fff"/></svg></div>
      <h3>VISION CARE</h3>
      <p>Lorem Ipsum is simply dummy text of the printing and typesetting industry. Lorem Ipsum has been.</p>
    </div>
    <div class="benefit">
      <div class="icon"><svg width="60" height="72" viewBox="0 0 60 72"><rect x="4" y="8" width="42" height="60" rx="3" fill="none" stroke="#fff" stroke-width="4"/><rect x="15" y="3" width="20" height="10" rx="2" fill="#fff"/><path d="M12 28h26M12 38h26M12 48h18" stroke="#fff" stroke-width="3"/><path d="M52 20v36l-3 7-3-7V20z" fill="#fff"/></svg></div>
      <h3>PRESCRIPTION</h3>
      <p>Lorem Ipsum is simply dummy text of the printing and typesetting industry. Lorem Ipsum has been.</p>
    </div>
    <div class="benefit">
      <div class="icon"><svg width="72" height="64" viewBox="0 0 72 64"><path d="M4 26L36 4l32 22v36H4z" fill="none" stroke="#fff" stroke-width="4"/><rect x="16" y="14" width="40" height="26" fill="#fff"/><path d="M22 22h28M22 30h28" stroke="#8a9a2d" stroke-width="3"/><path d="M4 26l32 22 32-22" stroke="#fff" stroke-width="4" fill="none"/></svg></div>
      <h3>MAIL ORDER</h3>
      <p>Lorem Ipsum is simply dummy text of the printing and typesetting industry. Lorem Ipsum has been.</p>
    </div>
  </div>
</section>
<section class="welcome">
  <div class="copy">
    <div class="mark"></div>
    <div class="kicker">WELCOME TO</div>
    <h2>The Allied Household</h2>
    <div class="sub">PROVISION ASSOCIATION</div>
    <p>Welcome to the Allied Senior Provision Association (ASPA). ASPA was started to be part of a senior-focused charitable organization that is different from other organizations with a similar perspective or mission.</p>
    <p>ASPA believes a charity should focus on raising money to support its mission, not its leaders. So, none of the ASPA officers or board members receive any compensation. Please read the description of what ASPA is about and how we go about raising money to support our mission.</p>
    <a class="btn">KNOW MORE</a>
  </div>
  <div class="photo" role="img" aria-label="Photo of a smiling older couple embracing"></div>
</section>
<section class="news">
  <span class="section-mark"></span>
  <h2 class="section-title">Latest News</h2>
  <div class="news-row">
    <article class="post">
      <div class="thumb" role="img" aria-label="Photo of an older couple relaxing at home" style="background:linear-gradient(135deg,#e4e2dc,#b8b1a8)"></div>
      <h3>Lorem Ipsum is simply dummy</h3>
      <p>Lorem Ipsum is simply dummy text of the printing and typesetting industry. Lorem Ipsum has been. Ipsum has been.</p>
    </article>
    <article class="post">
      <div class="thumb" role="img" aria-label="Photo of a woman with a tablet by a window" style="background:linear-gradient(135deg,#f0eee2,#b7b89a)"></div>
      <h3>Lorem Ipsum is simply dummy</h3>
      <p>Lorem Ipsum is simply dummy text of the printing and typesetting industry. Lorem Ipsum has been. Ipsum has been.</p>
    </article>
    <article class="post">
      <div class="thumb" role="img" aria-label="Photo of business people meeting in an office" style="background:linear-gradient(135deg,#eceff1,#9aa0a6)"></div>
      <h3>Lorem Ipsum is simply dummy</h3>
      <p>Lorem Ipsum is simply dummy text of the printing and typesetting industry. Lorem Ipsum has been. Ipsum has been.</p>
    </article>
  </div>
</section>
<section class="enroll">
  <h2>Free Membership Enrollment Form</h2>
  <div class="field">Enter Name*</div>
  <div class="field">Enter Email*</div>
  <div class="outline">KNOW MORE</div>
</section>
<footer class="footer">
  <div class="brand-foot">Allied Household Provision Association</div>
  <div class="col links">
    <h4>USEFULL LINKS</h4>
    <ul><li>Home</li><li>About</li><li>Benefits</li><li>News</li><li>Charities</li><li>Membership</li><li>Contact</li></ul>
  </div>
  <div class="col events">
    <h4>CONTACT US</h4>
    <div class="item">Lorem Ipsum is simply dummy text of<div class="date"><svg width="14" height="14"><rect width="14" height="14" rx="2" fill="#fed200"/><path d="M2 5h10" stroke="#8a9a2d" stroke-width="2"/></svg>Today 2:10 pm - 30.05.2017</div></div>
    <div class="item">Lorem Ipsum is simply dummy text of<div class="date"><svg width="14" height="14"><rect width="14" height="14" rx="2" fill="#fed200"/><path d="M2 5h10" stroke="#8a9a2d" stroke-width="2"/></svg>Today 2:10 pm - 30.05.2017</div></div>
    <div class="item">Lorem Ipsum is simply dummy text of<div class="date"><svg width="14" height="14"><rect width="14" height="14" rx="2" fill="#fed200"/><path d="M2 5h10" stroke="#8a9a2d" stroke-width="2"/></svg>Today 2:10 pm - 30.05.2017</div></div>
  </div>
  <div class="col contact">
    <h4>CONTACT US</h4>
    <div class="row"><svg width="18" height="24" viewBox="0 0 18 24"><path d="M9 1a8 8 0 00-8 8c0 6 8 14 8 14s8-8 8-14a8 8 0 00-8-8z" fill="none" stroke="#fed200" stroke-width="2"/><circle cx="9" cy="9" r="3" fill="#fed200"/></svg><div><strong>The Allied Household</strong><br>Lorem Ipsum is simply dummy print text of industry.</div></div>
    <div class="row"><svg width="18" height="18" viewBox="0 0 18 18"><path d="M3 1l4 4-2 3c1 2 3 4 5 5l3-2 4 4-3 3C7 18 0 11 0 4z" fill="#fed200"/></svg><div>+123 456 7890</div></div>
    <div class="row"><svg width="18" height="14" viewBox="0 0 18 14"><rect x="1" y="1" width="16" height="12" fill="none" stroke="#fed200" stroke-width="2"/><path d="M1 1l8 6 8-6" stroke="#fed200" stroke-width="2" fill="none"/></svg><div>info@alliedhousehold.org</div></div>
    <div class="social"><span role="img" aria-label="Social link"></span><span role="img" aria-label="Social link"></span><span role="img" aria-label="Social link"></span></div>
  </div>
  <div class="copyright">©The Allied Household Provision Association (AHPA) &nbsp; - 2017, All rights resreved.</div>
</footer>
</body>
</html>
```